Harbor of Mercy - Team of Rabbis and Doctors Helping Families Dealing with Illness

The Harbor of Mercy is an organization that accompanies families dealing with severe illnesses of a family member. A team of rabbis and doctors provide support and real-time responses to these families.
The site theme is medicine and law, but the target market is religious Jewish families in crisis. Thus, the site design needs to combine:
- professional, conservative, serious
- spiritual
- warm hug

Target Market(s)

religious families suffering a health crisis

Industry/Entity Type

Non-profit organization

Number of Pages Required

1 page

Font styles to use
Sans Serif

Requirements
Must have
• Final design in PSD format. List of fonts used, colors used and link/button colors used in the design.

```html
<!DOCTYPE html>
<html lang="en">
<head>
<meta charset="utf-8">
<title>Harbor of Mercy</title>
<link href="https://fonts.googleapis.com/css2?family=Montserrat:wght@400;500;600&display=swap" rel="stylesheet">
<style>
:root{
  --coral:#f5a98c;
  --green:#6dd3b1;
  --ink:#141414;
  --muted:#8a8a8a;
  --dark:#0b0b0b;
  --maroon:#1c0707;
  --white:#ffffff;
}
*{margin:0;padding:0;box-sizing:border-box}
html,body{width:1200px;height:3807px;overflow:hidden}
body{position:relative;background:var(--white);font-family:"Montserrat",Arial,sans-serif;color:var(--ink)}
.abs{position:absolute}
a{color:inherit}

/* top bar */
.topbar{left:0;top:0;width:1200px;height:47px;background:var(--dark)}
.search{left:99px;top:7px;width:344px;height:33px;background:var(--white);border-radius:17px;font-size:13px;line-height:33px;padding-left:10px}
.search svg{position:absolute;right:12px;top:9px}
.social{left:455px;top:8px;width:32px;height:32px;border-radius:50%;background:#14a6a0}
.toplink{top:13px;color:var(--white);font-size:17px;font-weight:500}

/* nav */
.nav-item{top:78px;font-size:16.5px;font-weight:500}
.brand{left:909px;top:66px;width:192px;font-size:24px;font-weight:600;color:var(--green);text-align:right;white-space:nowrap}

/* hero */
.hero{left:0;top:133px;width:1200px;height:466px;
  background:
    radial-gradient(ellipse 160px 200px at 300px 200px,rgba(255,214,150,.75) 0%,rgba(230,160,80,.35) 45%,transparent 100%),
    radial-gradient(ellipse 420px 300px at 260px 260px,rgba(190,120,60,.55) 0%,transparent 100%),
    radial-gradient(ellipse 300px 220px at 520px 120px,rgba(140,90,50,.45) 0%,transparent 100%),
    linear-gradient(90deg,#6b4a2e 0%,#4a3221 35%,#2a1d13 65%,#17110b 100%)}
.hero-title{right:100px;top:250px;text-align:right;color:var(--white);font-size:51px;font-weight:500;line-height:68px;letter-spacing:.5px}
.btn{border-radius:28px;background:var(--coral);color:var(--white);font-weight:500;display:flex;align-items:center;justify-content:center;gap:10px}
.btn-back{border-radius:28px;background:var(--green)}
.vline{width:2px;background:var(--coral)}

/* about */
.about-photo{left:99px;top:677px;width:471px;height:464px;border-radius:37px;
  background:
    radial-gradient(ellipse 200px 150px at 230px 220px,rgba(214,160,112,.7) 0%,rgba(150,100,64,.35) 50%,transparent 100%),
    radial-gradient(ellipse 90px 90px at 110px 250px,rgba(200,150,110,.55) 0%,transparent 100%),
    radial-gradient(ellipse 90px 90px at 360px 270px,rgba(200,150,110,.5) 0%,transparent 100%),
    linear-gradient(180deg,#0c0a09 0%,#2a1f17 40%,#1a130e 70%,#000 100%)}
.play{left:481px;top:1053px;width:76px;height:76px;border-radius:50%;background:var(--white);border:4px solid var(--green)}
.h2{font-size:44px;font-weight:500}
.h2 span{color:var(--green)}
.body-text{font-size:14.5px;line-height:21.5px;color:var(--muted)}

/* moral */
.moral{left:0;top:1253px;width:1200px;height:584px;
  background:
    radial-gradient(ellipse 60px 90px at 1100px 130px,rgba(255,230,180,.9) 0%,rgba(240,170,90,.4) 50%,transparent 100%),
    radial-gradient(ellipse 50px 80px at 580px 110px,rgba(255,220,170,.6) 0%,transparent 100%),
    radial-gradient(ellipse 220px 260px at 1080px 300px,rgba(200,130,50,.55) 0%,transparent 100%),
    radial-gradient(ellipse 200px 260px at 820px 260px,rgba(160,120,95,.5) 0%,transparent 100%),
    radial-gradient(ellipse 700px 420px at 75% 40%,#5e3f22 0%,#2e1e11 50%,#0a0705 85%)}
.moral-text{left:103px;top:1528px;width:430px;color:var(--white);font-size:14.5px;line-height:21.5px;font-weight:500}
.card{top:1783px;width:234px;height:239px}
.card-tab{top:1741px;height:42px;background:var(--coral);color:var(--white);font-size:23px;font-weight:500;text-align:center;line-height:42px}
.card-copy{position:absolute;left:8px;right:8px;top:150px;color:var(--white);font-size:9.5px;line-height:14px;text-align:center}
.card-more{position:absolute;left:0;right:0;top:203px;text-align:center;color:var(--white);font-size:15px;font-weight:600;text-decoration:underline}

/* testimonials */
.quote-card{top:2217px;width:487px;height:287px;border-radius:20px;background:var(--white);box-shadow:0 2px 10px rgba(0,0,0,.12)}
.quote-card .name{position:absolute;left:36px;top:30px;font-size:21px;font-weight:500}
.quote-card .role{position:absolute;left:36px;top:60px;font-size:16px;color:#555}
.quote-card .rule{position:absolute;left:36px;top:96px;width:407px;height:1px;background:#ddd}
.quote-card .mark{position:absolute;left:402px;top:36px}
.quote-card p{position:absolute;left:36px;top:128px;width:410px;font-size:12.5px;line-height:21.5px;color:var(--muted)}

/* news */
.news-photo{top:2678px;width:316px;height:241px}
.news-title{top:2930px;font-size:26px;font-weight:500}
.news-more{top:2970px;font-size:15px;text-decoration:underline;color:#555}

/* ask */
.ask-photo{left:0;top:3071px;width:596px;height:278px;
  background:
    radial-gradient(ellipse 130px 150px at 170px 120px,rgba(220,170,140,.75) 0%,transparent 100%),
    radial-gradient(ellipse 140px 120px at 420px 180px,rgba(200,110,110,.45) 0%,transparent 100%),
    linear-gradient(90deg,#44523c 0%,#6d7258 35%,#b4a58c 70%,#d8cbb6 100%)}
.ask-panel{left:596px;top:3071px;width:604px;height:278px;background:var(--maroon)}

/* newsletter */
.subscribe{left:197px;top:3522px;width:806px;height:79px;border:1px solid #cfcfcf;border-radius:40px}

/* footer */
.foot-item{top:3660px;font-size:21px;font-weight:500;transform:translateX(-50%)}
.foot-rule{left:99px;top:3732px;width:1002px;border-top:2px dotted #999}
.copy{left:0;top:3760px;width:1200px;text-align:center;font-size:14.5px}
</style>
</head>
<body>

<header>
  <div class="abs topbar"></div>
  <div class="abs search">Search
    <svg width="15" height="15" viewBox="0 0 15 15"><circle cx="6" cy="6" r="4.5" fill="none" stroke="#111" stroke-width="2"/><line x1="9.5" y1="9.5" x2="13.5" y2="13.5" stroke="#111" stroke-width="2.4"/></svg>
  </div>
  <div class="abs social" aria-label="Social page"></div>
  <div class="abs toplink" style="left:545px">Contact</div>
  <div class="abs toplink" style="left:652px">
    <svg width="13" height="13" viewBox="0 0 24 24"><path fill="#fff" d="M6.6 10.8a15 15 0 0 0 6.6 6.6l2.2-2.2a1 1 0 0 1 1-.25 11.4 11.4 0 0 0 3.6.57 1 1 0 0 1 1 1V20a1 1 0 0 1-1 1A17 17 0 0 1 3 4a1 1 0 0 1 1-1h3.5a1 1 0 0 1 1 1c0 1.25.2 2.45.57 3.57a1 1 0 0 1-.25 1z"/></svg>
    +1 555-010-2040</div>
  <div class="abs toplink" style="left:851px">Dedication 1</div>
  <div class="abs toplink" style="left:995px">Dedication 2</div>

  <nav>
    <a class="abs nav-item" style="left:97px;text-decoration:none">Home</a>
    <a class="abs nav-item" style="left:198px;text-decoration:none">About Us</a>
    <a class="abs nav-item" style="left:321px;text-decoration:none">Our Services</a>
    <a class="abs nav-item" style="left:470px;text-decoration:none">Testimonials</a>
    <a class="abs nav-item" style="left:622px;text-decoration:none">Blog</a>
    <a class="abs nav-item" style="left:704px;text-decoration:none">Contact Us</a>
  </nav>
  <div class="abs brand">Harbor of Mercy</div>
</header>

<section>
  <div class="abs hero" role="img" aria-label="Family lighting candles together at a warm candlelit table"></div>
  <h1 class="abs hero-title">SHOULD MORPHINE BE<br>GIVEN TO THE PATIENT?</h1>
  <div class="abs btn-back" style="left:882px;top:408px;width:200px;height:55px"></div>
  <div class="abs btn" style="left:896px;top:408px;width:202px;height:55px;font-size:21px">Get Started
    <svg width="18" height="18" viewBox="0 0 18 18"><circle cx="9" cy="9" r="9" fill="#fff"/><path d="M5 9h7M9 5.5 12.5 9 9 12.5" stroke="#f5a98c" stroke-width="2" fill="none"/></svg>
  </div>
  <svg class="abs" style="left:1064px;top:490px" width="40" height="22" viewBox="0 0 40 22"><path d="M9 3 2 11l7 8" stroke="#bbb" stroke-width="2" fill="none"/><path d="M30 3l7 8-7 8" stroke="#fff" stroke-width="3" fill="none"/></svg>
  <div class="abs vline" style="left:599px;top:566px;height:70px"></div>
</section>

<section>
  <div class="abs about-photo" role="img" aria-label="Portrait of a religious family in warm low light"></div>
  <div class="abs play"><svg width="68" height="68" viewBox="0 0 68 68"><path d="M29 23v22l17-11z" fill="#111"/></svg></div>
  <h2 class="abs h2" style="left:650px;top:680px">About <span>Us</span></h2>
  <p class="abs body-text" style="left:650px;top:757px;width:448px">Sed ut perspiciatis unde omnis iste natus error sit voluptatem accusantium doloremque laudantium, totam rem aperiam, eaque ipsa quae ab illo inventore veritatis et quasi architecto beatae vitae dicta sunt explicabo. Nemo enim ipsam voluptatem quia voluptas sit aspernatur aut odit aut fugit, sed quia consequuntur magni dolores eos qui ratione voluptatem sequi nesciunt. Neque porro quisquam est, qui dolorem ipsum quia dolor sit amet.</p>
  <p class="abs body-text" style="left:650px;top:958px;width:448px">Sed ut perspiciatis unde omnis iste natus error sit voluptatem accusantium doloremque laudantium, totam rem aperiam, eaque ipsa quae ab illo</p>
  <div class="abs btn-back" style="left:655px;top:1055px;width:200px;height:55px"></div>
  <div class="abs btn" style="left:670px;top:1055px;width:200px;height:55px;font-size:21px">Read More
    <svg width="18" height="18" viewBox="0 0 18 18"><circle cx="9" cy="9" r="9" fill="#fff"/><path d="M5 9h7M9 5.5 12.5 9 9 12.5" stroke="#f5a98c" stroke-width="2" fill="none"/></svg>
  </div>
  <div class="abs vline" style="left:599px;top:1224px;height:87px"></div>
</section>

<section>
  <div class="abs moral" role="img" aria-label="Elderly rabbi seated beside lit candles in a dim room"></div>
  <h2 class="abs h2" style="left:99px;top:1388px;color:#fff;line-height:54px">More Moral<br><span>Issues</span></h2>
  <p class="abs moral-text">Sed ut perspiciatis unde omnis iste natus error sit voluptatem accusantium doloremque laudantium, totam rem aperiam, eaque ipsa quae ab illo inventore veritatis et quasi architecto beatae vitae dicta sunt explicabo. Nemo</p>

  <div class="abs card-tab" style="left:106px;width:216px">Courses</div>
  <div class="abs card" style="left:97px;background:radial-gradient(ellipse 60px 80px at 90px 70px,rgba(60,60,70,.5) 0%,transparent 100%),linear-gradient(180deg,#e4e0da 0%,#b9b2aa 35%,#4a413b 75%,#1b1816 100%)" role="img" aria-label="Lecturer teaching a class">
    <p class="card-copy">Sed ut perspiciatis unde omnis iste natus error sit voluptatem accusantium doloremque laudantium, totam rem aperiam,</p>
    <div class="card-more">Read More</div>
  </div>

  <div class="abs card-tab" style="left:362px;width:216px">Conferences</div>
  <div class="abs card" style="left:355px;background:radial-gradient(ellipse 120px 70px at 120px 60px,rgba(190,120,110,.5) 0%,transparent 100%),linear-gradient(180deg,#a3978c 0%,#6e625a 40%,#3d3532 75%,#1a1716 100%)" role="img" aria-label="Crowd gathered at a conference">
    <p class="card-copy">Sed ut perspiciatis unde omnis iste natus error sit voluptatem accusantium doloremque laudantium, totam rem aperiam,</p>
    <div class="card-more">Read More</div>
  </div>

  <div class="abs card-tab" style="left:618px;width:216px">Lectures</div>
  <div class="abs card" style="left:610px;background:radial-gradient(ellipse 70px 80px at 117px 80px,rgba(110,70,50,.6) 0%,transparent 100%),linear-gradient(180deg,#2e2926 0%,#1f1b19 75%,#111 100%)" role="img" aria-label="Listener at a lecture">
    <p class="card-copy">Sed ut perspiciatis unde omnis iste natus error sit voluptatem accusantium doloremque laudantium, totam rem aperiam,</p>
    <div class="card-more">Read More</div>
  </div>

  <div class="abs card-tab" style="left:876px;width:216px">Hotline 24/7</div>
  <div class="abs card" style="left:866px;background:linear-gradient(180deg,#556b7c 0%,#33465a 50%,#22303b 75%,#151d24 100%)" role="img" aria-label="Round-the-clock support hotline">
    <svg style="position:absolute;left:75px;top:10px" width="84" height="84" viewBox="0 0 84 84"><circle cx="42" cy="42" r="36" fill="none" stroke="#d8dde2" stroke-width="4"/><text x="42" y="50" text-anchor="middle" font-family="Montserrat, sans-serif" font-size="26" font-weight="600" fill="#d8dde2">24</text></svg>
    <p class="card-copy">Sed ut perspiciatis unde omnis iste natus error sit voluptatem accusantium doloremque laudantium, totam rem aperiam,</p>
    <div class="card-more">Read More</div>
  </div>
</section>

<section>
  <h2 class="abs h2" style="left:0;top:2118px;width:1200px;text-align:center">Our <span>Testimonials</span></h2>

  <div class="abs quote-card" style="left:97px">
    <div class="name">Daniel</div>
    <div class="role">Duis aute irure dolor</div>
    <svg class="mark" width="40" height="30" viewBox="0 0 40 30"><path d="M2 28V16C2 7 7 2 15 1v6c-4 1-6 4-6 8h7v13zM23 28V16c0-9 5-14 13-15v6c-4 1-6 4-6 8h7v13z" fill="#f5a98c"/></svg>
    <div class="rule"></div>
    <p>Nemo enim ipsam voluptatem quia voluptas sit aspernatur aut odit aut fugit, sed quia consequuntur magni dolores eos qui ratione voluptatem sequi nesciunt. Neque porro quisquam est, qui dolorem ipsum quia dolor sit amet, consectetur, adipisci velit, sed quia non numquam eius modi tempora incidunt ut labore et dolore magnam aliquam quaerat voluptatem.</p>
  </div>

  <div class="abs quote-card" style="left:613px">
    <div class="name">Daniel</div>
    <div class="role">Duis aute irure dolor</div>
    <svg class="mark" width="40" height="30" viewBox="0 0 40 30"><path d="M2 28V16C2 7 7 2 15 1v6c-4 1-6 4-6 8h7v13zM23 28V16c0-9 5-14 13-15v6c-4 1-6 4-6 8h7v13z" fill="#f5a98c"/></svg>
    <div class="rule"></div>
    <p>Nemo enim ipsam voluptatem quia voluptas sit aspernatur aut odit aut fugit, sed quia consequuntur magni dolores eos qui ratione voluptatem sequi nesciunt. Neque porro quisquam est, qui dolorem ipsum quia dolor sit amet, consectetur, adipisci velit, sed quia non numquam eius modi tempora incidunt ut labore et dolore magnam aliquam quaerat voluptatem.</p>
  </div>
  <div class="abs vline" style="left:599px;top:2547px;height:54px"></div>
</section>

<section>
  <h2 class="abs h2" style="left:0;top:2598px;width:1200px;text-align:center">Our <span>News</span></h2>

  <div class="abs news-photo" style="left:99px;background:radial-gradient(ellipse 110px 90px at 120px 170px,rgba(150,110,80,.5) 0%,transparent 100%),linear-gradient(120deg,#ecebe7 0%,#c9c4bd 35%,#6f6862 65%,#2f2a28 100%)" role="img" aria-label="Father reading a book with his daughter"></div>
  <div class="abs news-title" style="left:99px">Voluptatem Quia</div>
  <div class="abs news-more" style="left:100px">Read More</div>

  <div class="abs news-photo" style="left:442px;background:radial-gradient(ellipse 200px 40px at 158px 150px,rgba(255,200,120,.8) 0%,transparent 100%),linear-gradient(180deg,#e7a661 0%,#c57a3c 35%,#7a4420 60%,#2b1a10 100%)" role="img" aria-label="Man facing a candlelit old city at dusk"></div>
  <div class="abs news-title" style="left:443px">Voluptatem Quia</div>
  <div class="abs news-more" style="left:444px">Read More</div>

  <div class="abs news-photo" style="left:786px;background:radial-gradient(ellipse 80px 60px at 170px 170px,rgba(255,220,160,.85) 0%,transparent 100%),radial-gradient(ellipse 90px 90px at 240px 100px,rgba(230,210,190,.7) 0%,transparent 100%),linear-gradient(135deg,#4a3526 0%,#8c6a4c 50%,#d9c2a4 100%)" role="img" aria-label="Grandmother and child lighting holiday candles"></div>
  <div class="abs news-title" style="left:787px">Voluptatem Quia</div>
  <div class="abs news-more" style="left:788px">Read More</div>

  <div class="abs vline" style="left:599px;top:3030px;height:66px"></div>
</section>

<section>
  <div class="abs ask-photo" role="img" aria-label="Smiling rabbi with a family in a bright living room"></div>
  <div class="abs ask-panel"></div>
  <h2 class="abs h2" style="left:671px;top:3124px;color:#fff">Ask the rabbi</h2>
  <p class="abs" style="left:671px;top:3205px;width:420px;color:#fff;font-size:12.5px;line-height:21.5px">Nemo enim ipsam voluptatem quia voluptas sit aspernatur aut odit aut fugit, sed quia consequuntur magni dolores eos qui ratione voluptatem sequi nesciunt. Neque porro quisquam est, qui dolorem ipsum quia dolor sit amet, consectetur, adipisci velit.</p>
</section>

<section>
  <h2 class="abs h2" style="left:0;top:3427px;width:1200px;text-align:center">Subscribe <span>Newsletter</span></h2>
  <div class="abs subscribe">
    <span style="position:absolute;left:43px;top:29px;font-size:15.5px;font-weight:500">Enter Your Email</span>
  </div>
  <div class="abs btn" style="left:814px;top:3535px;width:175px;height:54px;font-size:21px">Send Now</div>
</section>

<footer>
  <div class="abs foot-item" style="left:194px">Home</div>
  <div class="abs foot-item" style="left:337px">About Us</div>
  <div class="abs foot-item" style="left:507px">Our Services</div>
  <div class="abs foot-item" style="left:695px">Testimonials</div>
  <div class="abs foot-item" style="left:841px">Blog</div>
  <div class="abs foot-item" style="left:979px">Contact Us</div>
  <div class="abs foot-rule"></div>
  <div class="abs copy">© copyrights 2023 Harbor of Mercy | &nbsp;All Rights Reserved</div>
</footer>

</body>
</html>
```